Not-for-Profit Dog Breeding Association require interactive website

TWIG is an Australian based Not-for-Profit Association established to support the pet industry. We aim to provide member services, as well as a public access portal for consumers. We are looking for an inspired web design team who can create a multi function website experience that meets the following three requirements.

1. Member portal for pet breeders
2. Consumer portal with various links and resources
3. Sales platform for breeders to list advertisements

10-12 Pages including the following functionality:
- Built on a quality content management system like wordpress
- Searchable Members register
- Public resources section
- Member log-in, registration and application templates
- Members only pages and resources
- Payment portal to process member payments
- Members Advertising Platform (ie. ability for members to list ads)
- Easy to use search and selling platform
- Links to Chatterloop and Social Media
- Key Wording and Findora SEO
- Detailed editable Member Profiling
- About the Association
- Contact and Support

Logo and text content provided, additional creative brand styling required. Looking for outstanding quality and creativity from experienced website designers. Our aim is to lead the pet industry into a gold standard of care and operation and our website must reflect this level of quality.

Slow in providing feedback

```html
<!DOCTYPE html>
<html lang="en">
<head>
<meta charset="utf-8">
<title>TWIG — The Working Independent Guild of Breeders</title>
<link href="https://fonts.googleapis.com/css2?family=Montserrat:wght@600;700;800&family=Roboto:wght@400;500;700&display=swap" rel="stylesheet">
<style>
:root{
  --brown:#6b3a17;
  --tan:#c59a6a;
  --tan-light:#d9b48a;
  --text:#222;
  --muted:#8a8a8a;
  --grey-bg:#f3f3f3;
  --footer:#2b2b2b;
  --white:#fff;
}
*{box-sizing:border-box;margin:0;padding:0}
html,body{width:1200px;height:3705px;overflow:hidden}
body{position:relative;font-family:'Roboto',sans-serif;color:var(--text);background:var(--white)}
.abs{position:absolute}
.heading{font-family:'Montserrat',sans-serif;font-weight:700;text-transform:uppercase;color:var(--brown)}
.heading em{font-style:normal;color:var(--tan)}
.btn{position:absolute;display:flex;align-items:center;justify-content:center;font-family:'Roboto',sans-serif;font-weight:700;font-size:14px;color:var(--white);background:var(--tan);border-radius:4px;text-transform:uppercase}

/* header */
.site-header{left:0;top:0;width:1200px;height:120px;background:var(--white)}
.brand{left:111px;top:22px}
.brand-name{font-family:'Montserrat',sans-serif;font-weight:700;font-size:56px;letter-spacing:10px;color:var(--brown);line-height:56px}
.brand-tag{font-family:'Montserrat',sans-serif;font-weight:700;font-size:7px;color:var(--brown);letter-spacing:.3px;margin-top:4px}
.btn-member{left:790px;top:14px;width:161px;height:49px;background:var(--brown)}
.btn-consumer{left:961px;top:14px;width:128px;height:49px}
.main-nav{left:466px;top:86px;display:flex;gap:26px;font-size:14px;font-weight:500;color:#666;text-transform:uppercase}
.main-nav .active{color:var(--tan)}
.search-icon{left:1075px;top:87px}

/* hero */
.hero{left:0;top:120px;width:1200px;height:650px;overflow:hidden}
.hero-photo{position:absolute;inset:0;background:radial-gradient(ellipse at 75% 40%,#d7c2a4 0%,#b98957 35%,#6e6a3a 70%,#4b5530 100%)}
.hero-wave{position:absolute;left:0;bottom:0}
.hero-card{left:111px;top:262px;width:452px;height:269px;background:rgba(255,255,255,.78);border-radius:10px;padding:36px 31px}
.hero-card h1{font-size:35px;line-height:1;margin-bottom:22px}
.hero-card p{font-size:16px;line-height:27px;font-weight:500;color:#222}
.btn-start{left:31px;top:177px;width:128px;height:49px}

/* about */
.about-art{left:111px;top:819px;width:421px;height:414px;background:var(--tan)}
.about-copy{left:599px;top:862px;width:490px}
.about-copy h2{font-size:35px;line-height:45px}
.about-copy p{margin-top:22px;font-size:14px;line-height:25.8px;color:var(--muted);text-align:justify}
.btn-read{left:599px;top:1134px;width:129px;height:49px}

/* education */
.education{left:0;top:1347px;width:1200px;height:660px;background:var(--grey-bg)}
.section-title{position:absolute;left:0;width:1200px;text-align:center;font-size:31px}
.edu-card{position:absolute;top:161px;width:309px;height:389px;background:var(--white);border-radius:8px;box-shadow:0 4px 14px rgba(0,0,0,.12);text-align:center}
.edu-photo{position:absolute;left:8px;top:9px;right:8px;height:204px}
.edu-card h3{position:absolute;top:238px;width:100%;font-family:'Roboto',sans-serif;font-size:16px;font-weight:700;color:var(--brown)}
.edu-card p{position:absolute;top:271px;left:20px;right:20px;font-size:14px;line-height:25.5px;color:var(--muted)}
.round-arrow{position:absolute;left:50%;bottom:-26px;margin-left:-26px;width:52px;height:52px;border-radius:50%;background:var(--tan);display:flex;align-items:center;justify-content:center}

/* membership */
.member-band{left:0;top:2007px;width:1200px;height:343px;background:linear-gradient(90deg,#5e3312 0%,#7c4820 45%,#8a5326 65%,#6a3914 100%)}
.member-title{top:2082px;color:var(--white);font-size:31px}
.tier{position:absolute;width:231px;height:295px;background:var(--white);box-shadow:0 4px 14px rgba(0,0,0,.12);text-align:center}
.tier-icon{position:absolute;left:66px;top:33px;width:98px;height:98px;border-radius:50%;background:var(--tan);display:flex;align-items:center;justify-content:center}
.tier h3{position:absolute;top:162px;width:100%;font-size:16px;font-weight:700;color:var(--brown);text-transform:uppercase}
.tier p{position:absolute;top:193px;left:10px;right:10px;font-size:14px;line-height:25.5px;color:var(--muted)}

/* testimonials */
.quote-card{position:absolute;top:2685px;width:407px;height:232px;background:var(--white);border-radius:32px;box-shadow:0 4px 16px rgba(0,0,0,.13)}
.avatar{position:absolute;left:-42px;top:71px;width:94px;height:94px;border-radius:50%;background:linear-gradient(135deg,#c9b59b,#6f7d6a)}
.quote-mark{position:absolute;left:81px;top:30px;font-family:'Montserrat',sans-serif;font-weight:800;font-size:48px;line-height:48px;color:var(--tan)}
.quote-card p{position:absolute;left:81px;top:75px;right:26px;font-size:12px;line-height:22px;color:var(--muted);text-align:justify}
.quote-card h4{position:absolute;left:81px;top:170px;font-size:16px;font-weight:700;color:var(--brown);text-transform:uppercase}
.stars{position:absolute;left:81px;top:193px;font-size:11px;color:#f5a623;letter-spacing:1px}

/* non-profit */
.nonprofit{left:0;top:3022px;width:1200px;height:349px;background:linear-gradient(90deg,#b08252,#c59a6a 50%,#b68958)}
.nonprofit h2{position:absolute;top:62px;width:100%;text-align:center;font-size:31px;color:var(--white)}
.nonprofit p{position:absolute;top:124px;left:138px;width:924px;text-align:center;font-size:14px;line-height:26px;color:var(--white)}
.btn-donate{left:527px;top:230px;width:146px;height:49px;background:var(--white);color:var(--brown)}

/* footer */
.site-footer{left:0;top:3371px;width:1200px;height:334px;background:var(--footer);color:var(--white)}
.footer-brand{position:absolute;left:0;top:50px;width:1200px;text-align:center}
.footer-brand .brand-name{color:var(--white);font-size:64px;line-height:64px;letter-spacing:14px}
.footer-brand .brand-tag{color:var(--white);font-size:8px}
.footer-nav{position:absolute;top:163px;left:0;width:1200px;display:flex;justify-content:center;gap:36px;font-size:14px;font-weight:700;text-transform:uppercase}
.footer-contact{position:absolute;top:198px;left:0;width:1200px;display:flex;justify-content:center;align-items:center;gap:14px;font-size:15px}
.footer-rule{position:absolute;top:255px;height:1px;background:#777}
.social{position:absolute;left:582px;top:237px;width:36px;height:36px;border-radius:50%;background:var(--tan);display:flex;align-items:center;justify-content:center;font-size:8px;font-weight:700}
.copyright{position:absolute;left:0;width:1200px;top:288px;text-align:center;font-size:12px}
.pay-cards{position:absolute;left:921px;top:285px;display:flex;gap:3px}
.pay-cards span{width:31px;height:19px;background:var(--white);border-radius:2px;color:var(--brown);font-size:6px;font-weight:700;display:flex;align-items:center;justify-content:center}
</style>
</head>
<body>

<header class="abs site-header">
  <div class="abs brand">
    <div class="brand-name">TWIG</div>
    <div class="brand-tag">THE WORKING INDEPENDENT GUILD OF BREEDERS</div>
  </div>
  <a class="btn btn-member">Member Log In</a>
  <a class="btn btn-consumer">Consumer</a>
  <nav class="abs main-nav">
    <span class="active">Home</span><span>About Us</span><span>Education</span><span>Membership</span><span>Resources</span><span>Contact Us</span>
  </nav>
  <svg class="abs search-icon" width="14" height="14" viewBox="0 0 14 14"><circle cx="6" cy="6" r="4.5" fill="none" stroke="#666" stroke-width="2"/><line x1="9.3" y1="9.3" x2="13" y2="13" stroke="#666" stroke-width="2"/></svg>
</header>

<section class="abs hero">
  <div class="hero-photo" role="img" aria-label="Woman in a green sweater hugging a beagle outdoors in warm sunlight"></div>
  <svg class="hero-wave" width="1200" height="220" viewBox="0 0 1200 220" preserveAspectRatio="none">
    <path d="M0 220 L0 85 C160 20 320 10 520 70 C720 130 900 150 1200 90 L1200 220 Z" fill="#fff"/>
    <path d="M0 85 C160 20 320 10 520 70 C720 130 900 150 1200 90 L1200 98 C900 160 720 140 520 80 C320 22 170 34 0 95 Z" fill="var(--brown)"/>
    <path d="M520 80 C720 140 900 160 1200 98 L1200 110 C1000 190 740 200 560 110 Z" fill="var(--tan)"/>
  </svg>
  <div class="abs hero-card">
    <h1 class="heading">Welcome to <em>TWIG</em></h1>
    <p>Sed ut perspiciatis unde omnis iste natus error sit tatem accusantium doloremque lauda.</p>
    <a class="btn btn-start">Get Started</a>
  </div>
</section>

<div class="abs about-art" role="img" aria-label="Large letter shape with a dog illustration in tan"></div>
<div class="abs about-copy">
  <h2 class="heading">About<br><em>The Association</em></h2>
  <p>Lorem ipsum dolor sit amet, consectetur adipiscing elit, sed do eiusmod tempor incididunt ut labore et dolore magna aliqua. Ut enim ad minim veniam, quis nostrud exercitation ullamco laboris nisi ut aliquip ex ea commodo consequat. Duis aute irure dolor in reprehenderit in voluptate velit esse cillum dolore eu fugiat nulla pariatur.</p>
</div>
<a class="btn btn-read">Read More</a>

<section class="abs education">
  <h2 class="heading section-title" style="top:80px">Dog Breeders <em>Education</em></h2>
  <article class="edu-card" style="left:111px">
    <div class="edu-photo" role="img" aria-label="Man with a golden retriever in a sunny field" style="background:linear-gradient(135deg,#5a4630,#c8a064 60%,#e8c890)"></div>
    <h3>LOREM IPSUM DOLOR</h3>
    <p>Lorem ipsum dolor sit amet, consectetur adipiscing elit, sed do eiusmod tempor incididunt ut laborea.</p>
    <span class="round-arrow"><svg width="14" height="20" viewBox="0 0 14 20"><path d="M3 2 L11 10 L3 18" fill="none" stroke="#fff" stroke-width="2.5"/></svg></span>
  </article>
  <article class="edu-card" style="left:446px">
    <div class="edu-photo" role="img" aria-label="Woman in a red vest kneeling beside a husky on a country path" style="background:linear-gradient(160deg,#c9b07a,#9a8a5c 50%,#b8a890)"></div>
    <h3>LOREM IPSUM DOLOR</h3>
    <p>Lorem ipsum dolor sit amet, consectetur adipiscing elit, sed do eiusmod tempor incididunt ut laborea.</p>
    <span class="round-arrow"><svg width="14" height="20" viewBox="0 0 14 20"><path d="M3 2 L11 10 L3 18" fill="none" stroke="#fff" stroke-width="2.5"/></svg></span>
  </article>
  <article class="edu-card" style="left:780px">
    <div class="edu-photo" role="img" aria-label="Terrier leaping to catch a frisbee on a green lawn" style="background:linear-gradient(180deg,#2f4a24,#4f7a2c 60%,#5fa02a)"></div>
    <h3>LOREM IPSUM DOLOR</h3>
    <p>Lorem ipsum dolor sit amet, consectetur adipiscing elit, sed do eiusmod tempor incididunt ut laborea.</p>
    <span class="round-arrow"><svg width="14" height="20" viewBox="0 0 14 20"><path d="M3 2 L11 10 L3 18" fill="none" stroke="#fff" stroke-width="2.5"/></svg></span>
  </article>
</section>

<div class="abs member-band" role="img" aria-label="Brown-toned photo of a woman with her dog"></div>
<h2 class="heading section-title member-title">Our Membership</h2>

<article class="tier" style="left:111px;top:2173px">
  <span class="tier-icon"><svg width="50" height="50" viewBox="0 0 50 50" fill="none" stroke="#fff" stroke-width="2"><circle cx="18" cy="13" r="6"/><path d="M6 44 V32 a12 12 0 0 1 24 0 V44"/><path d="M30 30 h12 v14 h-12"/><path d="M38 8 l3 3 l3 -3"/></svg></span>
  <h3>Provisional Breeder</h3>
  <p>Lorem ipsum dolor sit amet, con sectetur adipiscing elit, sed do eiusmod temporea.</p>
</article>
<article class="tier" style="left:360px;top:2207px">
  <span class="tier-icon"><svg width="50" height="50" viewBox="0 0 50 50" fill="none" stroke="#fff" stroke-width="2.5"><ellipse cx="14" cy="18" rx="4" ry="5"/><ellipse cx="24" cy="12" rx="4" ry="5"/><ellipse cx="34" cy="14" rx="4" ry="5"/><ellipse cx="40" cy="24" rx="4" ry="5"/><path d="M14 36 c0-10 8-14 14-12 c6 2 8 8 6 14 c-2 5-8 4-11 3 c-4 2-9 1-9-5z"/></svg></span>
  <h3>Registered Kennel</h3>
  <p>Lorem ipsum dolor sit amet, con sectetur adipiscing elit, sed do eiusmod temporea.</p>
</article>
<article class="tier" style="left:609px;top:2173px">
  <span class="tier-icon"><svg width="50" height="50" viewBox="0 0 50 50" fill="none" stroke="#fff" stroke-width="2"><circle cx="25" cy="25" r="16"/><path d="M20 34 V16 h7 a5 5 0 0 1 0 10 h-7 M26 26 l6 8"/></svg></span>
  <h3>Registered Kennel</h3>
  <p>Lorem ipsum dolor sit amet, con sectetur adipiscing elit, sed do eiusmod temporea.</p>
</article>
<article class="tier" style="left:858px;top:2207px">
  <span class="tier-icon"><svg width="50" height="50" viewBox="0 0 50 50" fill="none" stroke="#fff" stroke-width="2"><circle cx="20" cy="10" r="5"/><path d="M14 46 V24 a6 6 0 0 1 12 0 V46"/><path d="M28 46 V34 l8 -6 l4 4 v14"/></svg></span>
  <h3>Kennel Master</h3>
  <p>Lorem ipsum dolor sit amet, con sectetur adipiscing elit, sed do eiusmod temporea.</p>
</article>

<h2 class="heading section-title" style="top:2600px">What Our <em>Clients Say</em></h2>
<article class="quote-card" style="left:184px">
  <span class="avatar" role="img" aria-label="Portrait of a client"></span>
  <span class="quote-mark">“</span>
  <p>Lorem ipsum dolor sit amet, consectetur adipiscing elit, sed do eiusmod tempor incididunt ut labore et dolore magna aliqua ut enim ad minim veniam, quis nostrud exercitation ullamco.</p>
  <h4>Mara Quill</h4>
  <span class="stars">★★★★★</span>
</article>
<article class="quote-card" style="left:662px">
  <span class="avatar" role="img" aria-label="Portrait of a client" style="background:linear-gradient(135deg,#5d7a4a,#2f6fa6)"></span>
  <span class="quote-mark">“</span>
  <p>Lorem ipsum dolor sit amet, consectetur adipiscing elit, sed do eiusmod tempor incididunt ut labore et dolore magna aliqua ut enim ad minim veniam, quis nostrud exercitation ullamco.</p>
  <h4>Mara Quill</h4>
  <span class="stars">★★★★★</span>
</article>

<section class="abs nonprofit" role="img" aria-label="Tan-toned photo of dogs and their owners">
  <h2 class="heading">Non-Profit Organization</h2>
  <p>Lorem ipsum dolor sit amet, consectetur adipiscing elit, sed do eiusmod tempor incididunt ut labore et dolore magna aliqua. Ut enim ad minim veniam, quis nostrud exercitation ullamco laboris nisi ut aliquip ex ea commodo consequat. Duis aute irure dolor in reprehenderit in voluptate velit esse cillum dolore eu fugute irure dolor in reprehenderit in viat nulla pariatur.</p>
  <a class="btn btn-donate">Donate Now</a>
</section>

<footer class="abs site-footer">
  <div class="footer-brand">
    <div class="brand-name">TWIG</div>
    <div class="brand-tag">THE WORKING INDEPENDENT GUILD OF BREEDERS</div>
  </div>
  <nav class="footer-nav"><span>Home</span><span>About Us</span><span>Education</span><span>Membership</span><span>Resources</span><span>Contact Us</span></nav>
  <div class="footer-contact">
    <svg width="13" height="13" viewBox="0 0 16 16"><path d="M3 1 L6 1 L7 5 L5 6.5 C6 9 7 10 9.5 11 L11 9 L15 10 L15 13 C15 14 14 15 13 15 C6 15 1 10 1 3 C1 2 2 1 3 1Z" fill="var(--tan)"/></svg>
    <span>+1 (555) 010 2040</span><span>/</span>
    <svg width="14" height="11" viewBox="0 0 14 11"><rect width="14" height="11" rx="1" fill="var(--tan)"/><path d="M0 1 L7 6 L14 1" fill="none" stroke="#2b2b2b" stroke-width="1.2"/></svg>
    <span>info@twig.org</span>
  </div>
  <div class="footer-rule" style="left:111px;width:461px"></div>
  <div class="footer-rule" style="left:628px;width:461px"></div>
  <span class="social" aria-label="Chatterloop">Chatterloop</span>
  <div class="copyright">© 2022 <b>TWIG</b> &nbsp;|&nbsp; All Rights Reserved</div>
  <div class="pay-cards"><span>Paylo</span><span>Cardo</span><span>Vantix</span><span>Amerio</span><span>Disko</span></div>
</footer>

</body>
</html>
```